Estate Planning Law Firm opening new branch in Florida

I am an experienced estate planning attorney that recently relocated to Florida. Looking for a banner Ad to place on platforms such as YardLoop, Chatterly and Pixmora to create publicity for firm and new leads.

```html
<!DOCTYPE html>
<html lang="en">
<head>
<meta charset="UTF-8">
<title>Serenova Law Firm – Estate Planning Attorney Now in Florida</title>
<link rel="stylesheet" href="https://fonts.googleapis.com/css2?family=Montserrat:wght@400;600;700;800&display=swap">
<style>
  :root {
    --navy: #2b3a4c;
    --ink: #2e3a4a;
    --teal: #1b6b6b;
    --white: #ffffff;
    --photo-water: #3d6f9c;
    --photo-dusk: #c98a45;
    --photo-green: #4a5d3e;
    --photo-sky: #e8d3b4;
  }
  * { margin: 0; padding: 0; box-sizing: border-box; }
  html, body { width: 1200px; height: 1200px; overflow: hidden; background: var(--white); }
  body { font-family: "Montserrat", sans-serif; }

  .ad {
    position: relative;
    width: 1200px;
    height: 1200px;
    background: var(--white);
    overflow: hidden;
  }

  .ad__art { position: absolute; inset: 0; width: 1200px; height: 1200px; }

  .brand {
    position: absolute;
    top: 118px;
    right: 96px;
    display: flex;
    align-items: center;
    gap: 14px;
  }
  .brand__mark { width: 40px; height: 40px; background: var(--teal); }
  .brand__text { display: flex; flex-direction: column; align-items: center; }
  .brand__name {
    font-weight: 700;
    font-size: 46px;
    letter-spacing: 1px;
    color: var(--ink);
    line-height: 1;
  }
  .brand__sub {
    margin-top: 6px;
    font-weight: 400;
    font-size: 17px;
    letter-spacing: 1px;
    color: var(--ink);
    line-height: 1;
  }

  .headline {
    position: absolute;
    left: 111px;
    top: 244px;
    font-size: 66px;
    line-height: 75px;
    color: var(--ink);
  }
  .headline__light { display: block; font-weight: 400; }
  .headline__strong { display: block; font-weight: 800; color: var(--teal); }

  .cta {
    position: absolute;
    left: 93px;
    top: 651px;
    width: 489px;
    height: 117px;
    border-radius: 60px;
    background: var(--teal);
    color: var(--white);
    font-weight: 700;
    font-size: 42px;
    line-height: 44px;
    text-align: center;
    display: flex;
    align-items: center;
    justify-content: center;
  }

  .contact {
    position: absolute;
    display: flex;
    align-items: center;
    gap: 12px;
    color: var(--white);
    font-weight: 600;
    font-size: 29px;
    white-space: nowrap;
  }
  .contact svg { width: 46px; height: 46px; flex: none; }
  .contact--social { right: 53px; top: 1053px; }
  .contact--web { right: 413px; top: 1118px; }
  .contact--phone { right: 53px; top: 1120px; }
</style>
</head>
<body>
  <main class="ad">
    <svg class="ad__art" viewBox="0 0 1200 1200">
      <defs>
        <linearGradient id="photoTone" x1="0" y1="1" x2="1" y2="0">
          <stop offset="0" stop-color="var(--photo-water)"/>
          <stop offset="0.35" stop-color="#5d7d8e"/>
          <stop offset="0.55" stop-color="var(--photo-green)"/>
          <stop offset="0.8" stop-color="var(--photo-dusk)"/>
          <stop offset="1" stop-color="var(--photo-sky)"/>
        </linearGradient>
      </defs>
      <polygon class="ad__photo" role="img"
        aria-label="Photo of a waterfront city at dusk: marina with yachts, park, and high-rise residential towers"
        points="0,819 1200,420 1200,912 0,1212" fill="url(#photoTone)"/>
      <polygon class="ad__band" points="0,1212 1200,912 1200,1200 0,1200" fill="var(--navy)"/>
    </svg>

    <header class="brand">
      <span class="brand__mark"></span>
      <span class="brand__text">
        <span class="brand__name">SERENOVA</span>
        <span class="brand__sub">LAW FIRM, PLLC</span>
      </span>
    </header>

    <h1 class="headline">
      <span class="headline__light">Experienced</span>
      <span class="headline__strong">Estate</span>
      <span class="headline__strong">Planning</span>
      <span class="headline__strong">Attorney</span>
      <span class="headline__light">Now in Florida!</span>
    </h1>

    <div class="cta">Contact me<br>for a consultation!</div>

    <div class="contact contact--social">
      <span class="contact__text">@serenovalaw</span>
      <svg viewBox="0 0 46 46" aria-label="Pixmora">
        <rect x="3" y="3" width="40" height="40" rx="8" fill="none" stroke="var(--teal)" stroke-width="3"/>
      </svg>
    </div>

    <div class="contact contact--web">
      <span class="contact__text">serenovalaw.com</span>
      <svg viewBox="0 0 46 46" aria-label="Website">
        <g fill="none" stroke="var(--teal)" stroke-width="3">
          <circle cx="23" cy="23" r="19"/>
          <ellipse cx="23" cy="23" rx="8" ry="19"/>
          <line x1="4" y1="23" x2="42" y2="23"/>
          <path d="M8 13 H38 M8 33 H38"/>
        </g>
      </svg>
    </div>

    <div class="contact contact--phone">
      <span class="contact__text">+1-305-555-0142</span>
      <svg viewBox="0 0 46 46" aria-label="Phone">
        <circle cx="23" cy="23" r="20" fill="none" stroke="var(--teal)" stroke-width="3"/>
        <path d="M16 13 l4 -1 3 6 -3 2 c1 3 3 5 6 6 l2 -3 6 3 -1 4 c-9 1 -18 -8 -17 -17z"
              fill="none" stroke="var(--teal)" stroke-width="2.5" stroke-linejoin="round"/>
      </svg>
    </div>
  </main>
</body>
</html>
```